Business Card Design Project

We are VT Meridian, a recruitment company based in London. We require a new business card design in order to present our business. We work in a number of areas recruiting professional in areas such as engineering and rail. Most of our work is based in the Middle East so our cards must have a universal, professional feel.

Visit our website: http://www.vt-meridian.example.co.uk/ for more info

Industry/Entity Type

Business

Requirements
Must have
• Must be double sided

Must feature the companies logo on both sides of the card

Should incorporate the primary colours of the logo

Must be professional and contemporary, to fit in with the logo

Info: Name: Colin Prewett certRP MREC
Senior Recruitment Consultant
Address: 7 Quarry Row Fulwell London N41QZ
T: +44 (0)203 555 0147
M: +44 (0)7700 900 318
E: cprewett@vt-meridian.example.co.uk
W www.vt-meridian.example.co.uk
Nice to have
• A modern style card

```html
<!DOCTYPE html>
<html lang="en">
<head>
<meta charset="utf-8">
<title>VT Meridian — Business Card</title>
<link rel="stylesheet" href="https://fonts.googleapis.com/css2?family=Questrial&display=swap">
<style>
  :root {
    --backdrop: #d9d9d7;
    --card: #eeeeec;
    --band: #6f6f70;
    --ink: #6a6a6b;
    --ink-dark: #3f3f40;
    --teal: #1a9a82;
    --white: #ffffff;
  }
  * { box-sizing: border-box; margin: 0; padding: 0; }
  html, body {
    width: 1200px; height: 900px; overflow: hidden;
    background: var(--backdrop);
    font-family: "Questrial", "Helvetica Neue", Arial, sans-serif;
    color: var(--ink);
  }
  .sheet {
    width: 1200px; height: 900px;
    display: flex; flex-direction: column;
    align-items: center; justify-content: center; gap: 44px;
  }
  .card {
    position: relative;
    width: 640px; height: 388px;
    background: var(--card);
    box-shadow: 0 6px 18px rgba(0,0,0,.12);
    overflow: hidden;
  }

  /* Wordmark */
  .wordmark { display: flex; align-items: center; gap: 14px; }
  .wordmark-dot { width: 54px; height: 54px; border-radius: 50%; background: var(--teal); flex: none; }
  .wordmark-name { font-size: 54px; line-height: 1; letter-spacing: -0.5px; }
  .tagline { font-size: 10px; letter-spacing: 3.2px; text-transform: uppercase; margin-top: 6px; }

  /* Back side */
  .card-back .band {
    position: absolute; left: 96px; right: 0; top: 36px; height: 150px;
    background: var(--band);
    padding: 34px 0 0 36px;
  }
  .card-back .wordmark-name, .card-back .tagline { color: var(--white); }
  .card-back .tagline { padding-left: 68px; }
  .card-back .web {
    position: absolute; right: 36px; top: 216px;
    font-size: 13px; letter-spacing: 2.4px; color: var(--ink);
  }

  /* Front side */
  .card-front .tab {
    position: absolute; left: 0; top: 196px; width: 44px; height: 112px;
    background: var(--band);
  }
  .card-front .brand { position: absolute; left: 64px; top: 60px; }
  .card-front .wordmark-name { color: var(--ink); }
  .card-front .tagline { color: var(--ink); padding-left: 68px; }
  .person { position: absolute; left: 80px; top: 176px; }
  .person-name { font-size: 21px; color: var(--ink); }
  .person-role { font-size: 15px; color: var(--ink); margin-top: 3px; }
  .contact { position: absolute; left: 80px; top: 250px; list-style: none; font-size: 14px; line-height: 1.45; }
  .contact-label { display: inline-block; width: 22px; color: var(--teal); font-weight: 700; }
  .address {
    position: absolute; right: 36px; top: 176px; text-align: left;
    font-size: 13px; line-height: 1.45; color: var(--ink);
  }
  .address .web { font-weight: 700; color: var(--ink-dark); margin-top: 4px; display: block; }
</style>
</head>
<body>
<main class="sheet">

  <section class="card card-back" aria-label="Card back">
    <div class="band">
      <div class="wordmark">
        <span class="wordmark-dot"></span>
        <span class="wordmark-name">VT Meridian</span>
      </div>
      <p class="tagline">Professional &amp; Technical Recruitment</p>
    </div>
    <p class="web">www.vt-meridian.example.co.uk</p>
  </section>

  <section class="card card-front" aria-label="Card front">
    <span class="tab"></span>
    <div class="brand">
      <div class="wordmark">
        <span class="wordmark-dot"></span>
        <span class="wordmark-name">VT Meridian</span>
      </div>
      <p class="tagline">Professional &amp; Technical Recruitment</p>
    </div>

    <div class="person">
      <p class="person-name">Colin Prewett certRP MREC</p>
      <p class="person-role">Senior Recruitment Consultant</p>
    </div>

    <ul class="contact">
      <li><span class="contact-label">T</span>+44 (0)203 555 0147</li>
      <li><span class="contact-label">M</span>+44 (0)7700 900 318</li>
      <li><span class="contact-label">E</span>cprewett@vt-meridian.example.co.uk</li>
    </ul>

    <address class="address" style="font-style:normal">
      7 Quarry Row Fulwell<br>
      London N41QZ
      <span class="web">www.vt-meridian.example.co.uk</span>
    </address>
  </section>

</main>
</body>
</html>
```